Yoga class opening. Little schedule for JUNE JULY and AUGUST

Flyer to promote an opening yoga class. The color of the docx haven't to be respected.

We want something joyfull, professional, clean and serious.

About the logo we oppened a contest at the same time so at the moment there is no logo but the logo color will be simple.

The phone number will change so you can poste a random one for the design that i can change by myself.

i recieved many creation in both side BUT i want something in 1 side :)

Target Market(s)

Yoga student. all age

Industry/Entity Type

It Professional

Logo Text

Yoga fern

Font styles to use
Sans Serif

Requirements
Must have
• The text present on the docx
Nice to have
• Some symbols about yoga ( Namasté signs, mandala, ... )
Should not have
• Not too much details it has to be clear.

```html
<!DOCTYPE html>
<html lang="fr">
<head>
<meta charset="utf-8">
<title>Yoga Fern – Flyer d'ouverture</title>
<link href="https://fonts.googleapis.com/css2?family=Arimo:wght@400;700&family=Roboto+Condensed:wght@400;700&family=Kaushan+Script&display=swap" rel="stylesheet">
<style>
  :root {
    --green: #7cc242;
    --green-dark: #5ea52c;
    --blue: #0d4a9c;
    --blue-dark: #0a3677;
    --orange: #f5a623;
    --gold: #e8a52e;
    --medal-gold: #e2ac3c;
    --sky: #3a9fdc;
    --white: #ffffff;
    --ink: #1c1c1c;
    --date-blue: #1a5fb4;
    --panel: #f3f3f3;
    --footer: #141414;
    --stage: #e9e6e1;
  }
  * { margin: 0; padding: 0; box-sizing: border-box; }
  html, body { width: 907px; height: 1200px; overflow: hidden; background: var(--stage); }
  .canvas { position: relative; width: 907px; height: 1200px; }
  .flyer {
    position: absolute; left: 46px; top: 28px;
    width: 740px; height: 1040px;
    transform: scale(1.1); transform-origin: top left;
    background: var(--white); overflow: hidden;
    font-family: "Arimo", Arial, sans-serif; color: var(--ink);
    box-shadow: 0 4px 14px rgba(0,0,0,.18);
  }
  .abs { position: absolute; }
  .backdrop { left: 0; top: 0; }
  .medallion { left: 23px; top: 55px; }

  .brand { right: 12px; top: 30px; font: 700 34px "Roboto Condensed", sans-serif; color: var(--orange); letter-spacing: 1px; }
  .headline { right: 18px; text-align: right; color: var(--white); font-family: "Arimo", sans-serif; }
  .headline.new { top: 90px; font-weight: 700; font-size: 25px; color: var(--orange); }
  .headline.studio { top: 124px; font-size: 22px; }
  .headline.city { top: 152px; font-size: 28px; }

  .opening { right: 28px; text-align: right; }
  .opening .label { font-size: 28px; color: var(--orange); line-height: 1.1; }
  .opening .date { font: 700 34px "Arimo", sans-serif; color: var(--white); line-height: 1.2; }
  .opening .address { font-size: 14px; color: var(--white); line-height: 1.4; margin-top: 10px; }

  .intro { left: 25px; top: 468px; }
  .intro .script { font: 26px "Kaushan Script", cursive; color: var(--blue); }
  .intro .lead { font-size: 21px; color: var(--ink); margin-top: 2px; }

  .month-tag {
    left: 0; width: 116px; height: 22px; background: var(--footer);
    clip-path: polygon(0 0, 92% 0, 100% 50%, 92% 100%, 0 100%);
    font: 17px "Kaushan Script", cursive; color: var(--orange);
    padding-left: 24px; line-height: 22px;
  }
  .stage-title { left: 22px; font: 700 13px "Roboto Condensed", sans-serif; }
  .sessions { left: 22px; list-style: none; }
  .sessions li { height: 19.5px; font-size: 12px; white-space: nowrap; }
  .sessions .when { display: inline-block; width: 181px; font: 700 11px "Roboto Condensed", sans-serif; color: var(--date-blue); }

  .right-panel { left: 420px; top: 552px; width: 320px; height: 283px; background: linear-gradient(90deg, var(--panel), var(--white) 40%); }
  .workshop { left: 468px; }
  .workshop h3 { font: 700 13px "Roboto Condensed", sans-serif; line-height: 1.3; margin-bottom: 10px; }
  .workshop ul { list-style: none; }
  .workshop li { font-size: 12px; height: 19.5px; }

  .august-band { left: 0; top: 835px; width: 740px; height: 156px; background: var(--gold); }
  .august .when { color: var(--ink); }

  .annual { left: 456px; top: 848px; width: 248px; height: 87px; background: var(--blue); border-radius: 4px; text-align: center; color: var(--white); padding-top: 8px; }
  .annual .line { font-size: 13px; }
  .annual .day { font: 700 16px "Arimo", sans-serif; color: var(--orange); margin-top: 3px; }
  .annual .more { font: 18px "Kaushan Script", cursive; margin-top: 2px; }
  .farewell { left: 484px; top: 944px; font: 26px "Kaushan Script", cursive; color: var(--white); }

  .footer { left: 0; top: 991px; width: 740px; height: 49px; background: var(--footer); }
  .phone { left: 22px; top: 1001px; display: flex; align-items: center; gap: 8px; color: var(--white); font: 700 24px "Arimo", sans-serif; }
  .social { right: 50px; top: 1008px; font-size: 13px; color: var(--orange); }
  .social strong { color: var(--white); font-weight: 400; }
</style>
</head>
<body>
<div class="canvas">
  <div class="flyer">
    <svg class="abs backdrop" width="740" height="520" viewBox="0 0 740 520">
      <defs>
        <linearGradient id="greenGrad" x1="0" y1="0" x2="1" y2="1">
          <stop offset="0" stop-color="#86c94a"/>
          <stop offset="1" stop-color="#5ea52c"/>
        </linearGradient>
        <linearGradient id="blueGrad" x1="0" y1="0" x2="1" y2="0">
          <stop offset="0" stop-color="#0a3677"/>
          <stop offset="1" stop-color="#1558b0"/>
        </linearGradient>
      </defs>
      <polygon points="0,0 740,0 740,195 445,262 395,385 0,376" fill="url(#greenGrad)"/>
      <polygon points="0,372 395,381 392,390 0,381" fill="var(--orange)"/>
      <polygon points="445,262 740,195 740,462 395,385" fill="url(#blueGrad)"/>
      <polygon points="395,385 740,462 740,478 382,393" fill="var(--orange)"/>
    </svg>

    <svg class="abs medallion" width="372" height="372" viewBox="0 0 372 372" role="img" aria-label="Médaillon doré en forme de soleil autour d'une photo de deux personnes en posture de l'arbre au bord de la mer">
      <defs>
        <linearGradient id="photoGrad" x1="0" y1="0" x2="0" y2="1">
          <stop offset="0" stop-color="#5bb7e8"/>
          <stop offset="0.75" stop-color="#2c8fd0"/>
          <stop offset="1" stop-color="#1f6fa8"/>
        </linearGradient>
      </defs>
      <circle cx="186" cy="186" r="184" fill="var(--blue)"/>
      <circle cx="186" cy="186" r="176" fill="var(--medal-gold)"/>
      <circle cx="186" cy="186" r="144" fill="var(--blue-dark)"/>
      <circle cx="186" cy="186" r="140" fill="url(#photoGrad)"/>
    </svg>

    <div class="abs brand">YOGA FERN</div>
    <div class="abs headline new">NOUVEAU !!</div>
    <div class="abs headline studio">VOTRE STUDIO DE</div>
    <div class="abs headline city">YOGA A IXELLES</div>

    <div class="abs opening" style="top:283px">
      <div class="label">OUVERTURE LE</div>
      <div class="date">6 JUIN 2016 AU</div>
      <div class="address">212 RUE DES TILLEULS<br>1050 IXELLES</div>
    </div>

    <div class="abs intro">
      <p class="script">En attendant le planning des cours de la rentrée,</p>
      <p class="lead">YOGA FERN vous propose ses stages et ateliers d’été</p>
    </div>

    <div class="abs right-panel"></div>

    <div class="abs month-tag" style="top:545px">Juin</div>
    <p class="abs stage-title" style="top:574px">Stage découverte du YOGA 10h00 85 € :</p>
    <ul class="abs sessions" style="top:604px">
      <li><span class="when">Du lundi 6 au vendredi 10 juin :</span>10h00 à 12h00 ou 18h00 à 20h00</li>
      <li><span class="when">Du lundi 13 au vendredi 17 juin :</span>10h00 à 12h00 ou 18h00 à 20h00</li>
      <li><span class="when">Du lundi 20 au vendredi 24 juin :</span>10h00 à 12h00 ou 18h00 à 20h00</li>
      <li><span class="when">Du lundi 27 au vendredi 1er juillet :</span>10h00 à 12h00 ou 18h00 à 20h00</li>
    </ul>

    <div class="abs month-tag" style="top:692px">Juillet</div>
    <p class="abs stage-title" style="top:718px">Stage initiation à l’ASHTANGA 10h00 85 €</p>
    <ul class="abs sessions" style="top:743px">
      <li><span class="when">Du lundi 4 au vendredi 8 juillet :</span>10h00 à 12h00 ou 18h00 à 20h00</li>
      <li><span class="when">Du lundi 11 au vendredi 15 juillet :</span>10h00 à 12h00 ou 18h00 à 20h00</li>
      <li><span class="when">Du lundi 18 au vendredi 22 juillet :</span>10h00 à 12h00 ou 18h00 à 20h00</li>
      <li><span class="when">Du lundi 25 au vendredi 29 juillet :</span>10h00 à 12h00 ou 18h00 à 20h00</li>
    </ul>

    <div class="abs workshop" style="top:567px">
      <h3>Atelier gestion du stress yoga/sophrologie<br>2h00 28 €</h3>
      <ul>
        <li>Samedi 11 juin 10h30 à 12h30</li>
        <li>Samedi 11 juin 15h à 17h00</li>
        <li>Dimanche 12 juin 10h30 à 12h30</li>
        <li>Dimanche 12 juin 14h à 16h00</li>
      </ul>
    </div>
    <div class="abs workshop" style="top:712px">
      <h3>Atelier gestion du stress yoga/sophrologie<br>2h00 28 €</h3>
      <ul>
        <li>Samedi 9 juillet 10h30 à 12h30</li>
        <li>Samedi 9 juillet 15h00 à 17h00</li>
        <li>Dimanche 10 juillet 10h30 à 12h30</li>
        <li>Dimanche 10 juillet 14h00 à 16h00</li>
      </ul>
    </div>

    <div class="abs august-band"></div>
    <div class="abs month-tag" style="top:844px">Aout</div>
    <p class="abs stage-title" style="top:872px; color:var(--white)">Stage découverte du YOGA 10h00 85 €</p>
    <ul class="abs sessions august" style="top:899px">
      <li><span class="when">Du lundi 1er au vendredi 5 août :</span>10h00 à 12h00 ou 18h00 à 20h00</li>
      <li><span class="when">Du lundi 8 au vendredi 12 août :</span>10h00 à 12h00 ou 18h00 à 20h00</li>
      <li><span class="when">Du lundi 15 au vendredi 19 août :</span>10h00 à 12h00 ou 18h00 à 20h00</li>
      <li><span class="when">Du lundi 22 au vendredi 26 août :</span>10h00 à 12h00 ou 18h00 à 20h00</li>
    </ul>

    <div class="abs annual">
      <p class="line">Démarrage du planning annuel le</p>
      <p class="day">5 septembre 2016</p>
      <p class="more">Plus d’info et inscription</p>
    </div>
    <p class="abs farewell">Un bel ete a tous!</p>

    <div class="abs footer"></div>
    <div class="abs phone">
      <svg width="18" height="18" viewBox="0 0 18 18" aria-hidden="true">
        <rect width="18" height="18" rx="3" fill="var(--orange)"/>
        <path d="M5.5 4h2l1 3-1.3 1a6 6 0 0 0 2.8 2.8l1-1.3 3 1v2a1.5 1.5 0 0 1-1.6 1.5A9 9 0 0 1 4 5.6 1.5 1.5 0 0 1 5.5 4z" fill="var(--footer)"/>
      </svg>
      0470 58 21 36
    </div>
    <p class="abs social">Ou via notre page Lotuspage : <strong>yoga fern</strong></p>
  </div>
</div>
</body>
</html>
```